Podcast website that will AMAZE

I need a Wordpress website designed for my podcast that I am about to launch. The podcast is called 'bright lantern warm harbor' and is targeted at 30-45 year old professional females. The podcast is aiming to provide listeners with information, from a variety of experts, to improve their health and well-being, but also their financial circumstances. I want a landing page that would appeal to this demographic that is clean and uncluttered. also, I want the ability to play the podcast episodes from the website by integrating with vorcast as the media host. I need the ability to capture their personal information and ability to provide downloadable documents to people who come to the website. Although I would not initially need a shopping cart I will need the ability to add one at a future date. I have attached the current logo to give you an idea of theme

Target Market(s)

30-45 year 0ld professional females with an interest in health

Coding

Coded - Design and coding required

Colors

Designer to choose colors to be used in the design.

Requirements
Must have
• - ability to play podcasts from website. will be using vorcast as media host
• - clean uncluttered layout
• - ability to capture emails from vistors
• - ability to include online store in the future

```html
<!DOCTYPE html>
<html lang="en">
<head>
<meta charset="utf-8">
<title>Bright Lantern Warm Harbor — Podcast</title>
<link href="https://fonts.googleapis.com/css2?family=Lora:ital,wght@0,400;0,700;1,400&family=Poppins:wght@400;500&display=swap" rel="stylesheet">
<style>
:root{
  --ink:#050608;
  --purple:#8e3a8c;
  --purple-deep:#6e2a6d;
  --plum:#a3458f;
  --blue:#1e9be0;
  --teal:#2aa7d8;
  --white:#ffffff;
  --text:#222222;
  --muted:#555555;
  --serif:'Lora', Georgia, serif;
  --sans:'Poppins', Arial, sans-serif;
}
*{box-sizing:border-box;margin:0;padding:0}
html,body{width:1200px;height:2413px;overflow:hidden;background:var(--white)}
body{position:relative;font-family:var(--serif);color:var(--text)}
.abs{position:absolute}

/* header */
.site-header{position:absolute;left:0;top:0;width:1200px;height:102px;background:var(--ink)}
.brand{position:absolute;left:100px;top:24px;display:flex;align-items:center;gap:12px}
.brand-dot{width:44px;height:44px;border-radius:50%;background:var(--purple)}
.brand-name{font-family:var(--serif);font-size:19px;line-height:21px;color:#c95aa6;font-weight:400;letter-spacing:.5px}
.main-nav{position:absolute;top:40px;left:528px;display:flex;gap:0}
.main-nav a{font-family:var(--serif);font-weight:700;font-size:13px;color:var(--white);text-decoration:none;position:absolute;white-space:nowrap}
.search-icon{position:absolute;left:1089px;top:43px}

/* hero */
.hero{position:absolute;left:0;top:102px;width:1200px;height:505px;overflow:hidden;
  background:radial-gradient(ellipse at 28% 40%,#6b6e73 0%,#3b4150 28%,#1d2740 55%,#121a30 100%)}
.hero-title{position:absolute;right:100px;top:86px;text-align:right;color:var(--white);font-family:var(--serif);font-weight:700;font-size:52px;line-height:70px;letter-spacing:1px}
.hero-sub{position:absolute;right:100px;top:232px;text-align:right;color:var(--white);font-family:var(--serif);font-weight:700;font-size:21px;line-height:28px}
.wave{position:absolute;left:0;top:0}
.time{position:absolute;top:458px;color:var(--white);font-family:var(--serif);font-weight:700;font-size:13px}

/* podcasts */
.podcasts{position:absolute;left:0;top:607px;width:1200px;height:690px;overflow:hidden;background:var(--white)}
.section-title{position:absolute;left:0;width:1200px;text-align:center;font-family:var(--serif);font-weight:700;color:#151515}
.podcasts .section-title{top:96px;font-size:35px}
.subtitle{position:absolute;top:152px;left:0;width:1200px;text-align:center;font-size:17px;color:var(--purple)}
.subtitle .accent{color:var(--teal)}
.card{position:absolute;width:300px;height:152px;border-radius:9px;overflow:hidden}
.card-title{position:absolute;left:24px;top:28px;font-family:var(--sans);font-weight:500;font-size:19px;color:var(--white);text-transform:uppercase}
.card-meta{position:absolute;left:24px;top:55px;font-family:var(--sans);font-size:14px;color:var(--white);text-transform:uppercase}
.card svg{position:absolute;left:0;top:0}

/* newsletter */
.newsletter{position:absolute;left:0;top:1297px;width:1200px;height:304px;background:linear-gradient(180deg,#2d8fd8 0%,#5a6bc4 40%,#8a45a6 75%,#97438f 100%)}
.newsletter .section-title{top:52px;font-size:32px;color:var(--white);font-weight:500}
.newsletter-copy{position:absolute;top:110px;left:0;width:1200px;text-align:center;color:var(--white);font-style:italic;font-size:15.5px;line-height:31px}
.subscribe{position:absolute;left:282px;top:188px;width:636px;height:49px;background:var(--white);border-radius:25px}
.subscribe .field{position:absolute;left:26px;top:16px;font-size:12px;color:#333}
.subscribe .btn{position:absolute;right:0;top:0;width:148px;height:49px;border-radius:25px;background:var(--blue);color:var(--white);font-weight:700;font-size:14px;text-align:center;line-height:49px}

/* experts */
.experts{position:absolute;left:0;top:1601px;width:1200px;height:557px;
  background:linear-gradient(135deg,#f1eee9 0%,#e5e6e8 35%,#c8ccd4 55%,#e4e1dc 80%,#efece7 100%)}
.experts .section-title{top:76px;font-size:30px}
.expert{position:absolute;top:0;width:330px;text-align:center}
.expert-name{position:absolute;top:364px;width:330px;font-weight:700;font-size:14px;color:#222;letter-spacing:.5px}
.expert-name.active{color:var(--purple)}
.expert-bio{position:absolute;top:393px;width:330px;font-size:12.5px;line-height:25px;color:#444}
.social{position:absolute;top:460px;left:138px;display:flex;gap:8px}
.social span{width:15px;height:15px;border-radius:50%;background:#2a2a2a;display:block}
.social.active span{background:var(--blue)}

/* footer */
.site-footer{position:absolute;left:0;top:2158px;width:1200px;height:208px;background:var(--purple)}
.footer-nav a{position:absolute;top:44px;color:var(--white);font-weight:700;font-size:13px;text-decoration:none;white-space:nowrap}
.footer-nav .sep{position:absolute;top:40px;color:var(--white);font-size:18px}
.footer-rule{position:absolute;left:100px;top:100px;width:1000px;height:1px;background:rgba(255,255,255,.6)}
.contact{position:absolute;top:132px;display:flex;align-items:center;gap:16px;color:var(--white);font-size:12px}
.contact-icon{width:38px;height:38px;border-radius:50%;background:var(--white);display:flex;align-items:center;justify-content:center}
.bottom-bar{position:absolute;left:0;top:2366px;width:1200px;height:47px;background:var(--purple-deep)}
.copyright{position:absolute;left:100px;top:17px;color:var(--white);font-size:12px}
.bottom-social{position:absolute;right:100px;top:18px;display:flex;gap:18px}
.bottom-social span{width:11px;height:11px;border-radius:50%;background:var(--white);display:block}
</style>
</head>
<body>

<header class="site-header">
  <div class="brand">
    <span class="brand-dot"></span>
    <span class="brand-name">BRIGHT LANTERN<br>WARM HARBOR</span>
  </div>
  <nav class="main-nav">
    <a style="left:0">Home</a>
    <a style="left:80px">About Us</a>
    <a style="left:180px">Podcast</a>
    <a style="left:273px">Contact us</a>
    <a style="left:381px">Resource</a>
    <a style="left:483px">Shop</a>
  </nav>
  <svg class="search-icon" width="14" height="14" viewBox="0 0 14 14" aria-hidden="true"><circle cx="5.5" cy="5.5" r="4" fill="none" stroke="#fff" stroke-width="2"/><path d="M8.5 8.5L12.5 12.5" stroke="#fff" stroke-width="2.2"/></svg>
</header>

<section class="hero">
  <div class="abs" role="img" aria-label="Studio condenser microphone in a recording booth with blurred mixing desk lights" style="left:0;top:0;width:1200px;height:505px;background:radial-gradient(ellipse 420px 360px at 300px 240px,rgba(150,150,150,.55),rgba(0,0,0,0))"></div>
  <h1 class="hero-title">BRIGHT LANTERN<br>WARM HARBOR</h1>
  <p class="hero-sub">Excepteur sint occaecat cupidatat non proident,<br>sunt in culpa qui officia deserunt</p>
  <svg class="wave" width="1200" height="505" viewBox="0 102 1200 505" aria-hidden="true">
    <path d="M100 525H835" stroke="#8a7fd6" stroke-width="2"/>
    <path stroke="#3b7de0" stroke-width="4" d="M104 519V531M125 517V533M146 505V545M167 507V543M188 509V541M209 503V547M230 501V549M251 497V553M272 503V547M293 495V555M314 499V551M335 491V559M356 495V555M377 487V563M398 493V557M419 489V561M440 497V553M461 495V555M482 501V549M503 497V553M524 505V545M545 485V565M566 507V543M587 481V569M608 505V545M629 483V567M650 509V541M671 487V563M692 511V539M713 493V557M734 513V537M755 497V553M776 515V535M797 511V539M818 515V535"/>
    <path stroke="#9a4fb5" stroke-width="4" d="M114.5 515V535M135.5 511V539M156.5 513V537M177.5 499V551M198.5 515V535M219.5 495V555M240.5 511V539M261.5 489V561M282.5 507V543M303.5 485V565M324.5 505V545M345.5 481V569M366.5 501V549M387.5 479V571M408.5 503V547M429.5 483V567M450.5 507V543M471.5 487V563M492.5 509V541M513.5 491V559M534.5 495V555M555.5 499V551M576.5 493V557M597.5 497V553M618.5 489V561M639.5 499V551M660.5 495V555M681.5 503V547M702.5 499V551M723.5 507V543M744.5 503V547M765.5 509V541M786.5 507V543M807.5 517V533M828.5 519V531"/>
    <circle cx="620" cy="525" r="7" fill="#fff"/><circle cx="620" cy="525" r="3" fill="#3b4aa0"/>
  </svg>
  <span class="time" style="left:100px">22.20</span>
  <span class="time" style="left:800px">36.02</span>
</section>

<section class="podcasts">
  <svg class="abs" style="left:0;top:0" width="200" height="210" viewBox="0 0 200 210" aria-hidden="true">
    <path d="M172 0A190 190 0 0 1 0 200" fill="none" stroke="var(--purple)" stroke-width="18"/>
  </svg>
  <h2 class="section-title">Play Podcasts</h2>
  <p class="subtitle"><span class="accent">Health</span> &amp; Finance education</p>

  <article class="card" style="left:100px;top:228px">
    <div class="abs" role="img" aria-label="Episode artwork: woman at a warmly lit evening market" style="inset:0;background:linear-gradient(135deg,#2a2626,#4a2f2e 60%,#1c1c1f)"></div>
    <h3 class="card-title">PDC 19 – Wavehall</h3><p class="card-meta">Harlow Play | 2017-11-11</p>
    <svg width="300" height="152" aria-hidden="true"><circle cx="39" cy="107" r="14" fill="#fff"/><path d="M35 100L46 107L35 114Z" fill="var(--blue)"/><path d="M64 107H248" stroke="#fff" stroke-width="3"/><path d="M262 103H266L271 98V116L266 111H262Z" fill="#fff"/></svg>
  </article>
  <article class="card" style="left:451px;top:228px">
    <div class="abs" role="img" aria-label="Episode artwork: hands holding a small plant" style="inset:0;background:linear-gradient(135deg,#5a3426,#7a4a36 50%,#3a2a26)"></div>
    <h3 class="card-title">PDC 19 – Wavehall</h3><p class="card-meta">Harlow Play | 2017-11-11</p>
    <svg width="300" height="152" aria-hidden="true"><circle cx="39" cy="107" r="14" fill="#fff"/><path d="M35 100L46 107L35 114Z" fill="var(--blue)"/><path d="M64 107H248" stroke="#fff" stroke-width="3"/><path d="M262 103H266L271 98V116L266 111H262Z" fill="#fff"/></svg>
  </article>
  <article class="card" style="left:802px;top:228px">
    <div class="abs" role="img" aria-label="Episode artwork: woman smiling among green plants" style="inset:0;background:linear-gradient(135deg,#3a3a34,#4f5a3c 55%,#2a2e26)"></div>
    <h3 class="card-title">PDC 19 – Wavehall</h3><p class="card-meta">Harlow Play | 2017-11-11</p>
    <svg width="300" height="152" aria-hidden="true"><circle cx="39" cy="107" r="14" fill="#fff"/><path d="M35 100L46 107L35 114Z" fill="var(--blue)"/><path d="M64 107H248" stroke="#fff" stroke-width="3"/><path d="M262 103H266L271 98V116L266 111H262Z" fill="#fff"/></svg>
  </article>
  <article class="card" style="left:100px;top:431px">
    <div class="abs" role="img" aria-label="Episode artwork: desk with piggy bank and paperwork from above" style="inset:0;background:linear-gradient(135deg,#25313a,#2d4656 55%,#1f2428)"></div>
    <h3 class="card-title">PDC 19 – Wavehall</h3><p class="card-meta">Harlow Play | 2017-11-11</p>
    <svg width="300" height="152" aria-hidden="true"><circle cx="39" cy="107" r="14" fill="#fff"/><path d="M35 100L46 107L35 114Z" fill="var(--blue)"/><path d="M64 107H248" stroke="#fff" stroke-width="3"/><path d="M262 103H266L271 98V116L266 111H262Z" fill="#fff"/></svg>
  </article>
  <article class="card" style="left:451px;top:431px">
    <div class="abs" role="img" aria-label="Episode artwork: financial planning notes beside stacked coins" style="inset:0;background:linear-gradient(135deg,#3a4434,#5a6450 55%,#2c2f2a)"></div>
    <h3 class="card-title">PDC 19 – Wavehall</h3><p class="card-meta">Harlow Play | 2017-11-11</p>
    <svg width="300" height="152" aria-hidden="true"><circle cx="39" cy="107" r="14" fill="#fff"/><path d="M35 100L46 107L35 114Z" fill="var(--blue)"/><path d="M64 107H248" stroke="#fff" stroke-width="3"/><path d="M262 103H266L271 98V116L266 111H262Z" fill="#fff"/></svg>
  </article>
  <article class="card" style="left:802px;top:431px">
    <div class="abs" role="img" aria-label="Episode artwork: coins and a jar on a table" style="inset:0;background:linear-gradient(135deg,#4a4440,#6a5e56 55%,#3a3430)"></div>
    <h3 class="card-title">PDC 19 – Wavehall</h3><p class="card-meta">Harlow Play | 2017-11-11</p>
    <svg width="300" height="152" aria-hidden="true"><circle cx="39" cy="107" r="14" fill="#fff"/><path d="M35 100L46 107L35 114Z" fill="var(--blue)"/><path d="M64 107H248" stroke="#fff" stroke-width="3"/><path d="M262 103H266L271 98V116L266 111H262Z" fill="#fff"/></svg>
  </article>
</section>

<section class="newsletter">
  <h2 class="section-title">Newsletter Subscription</h2>
  <p class="newsletter-copy">Lorem ipsum dolor sit amet, consectetur adipiscing elit, sed do eiusmod tempor incididunt<br>ut labore et dolore magna aliqua. Ut enim ad minim veniam, quis nostrud exercitation ullamco</p>
  <div class="subscribe"><span class="field">Email Id</span><span class="btn">SUBSCRIBE</span></div>
</section>

<section class="experts">
  <div class="abs" role="img" aria-label="Woman stretching on a mat in a bright living room, softly faded" style="inset:0;background:radial-gradient(ellipse 380px 280px at 560px 330px,rgba(120,135,160,.35),rgba(0,0,0,0))"></div>
  <h2 class="section-title">Meet The Experts</h2>

  <div class="expert" style="left:69px">
    <svg class="abs" style="left:73px;top:165px" width="184" height="184" aria-hidden="true"><path d="M92 8A84 84 0 1 1 30 34" fill="none" stroke="#fff" stroke-width="6"/><circle cx="92" cy="94" r="78" fill="#fff"/><path d="M142 0L146 10L156 11L148 17L151 27L142 21L133 27L136 17L128 11L138 10Z" fill="#fff"/></svg>
    <div class="abs" role="img" aria-label="Portrait photo of expert Mira Daven" style="left:169px;top:189px;width:0;height:0"></div>
    <div class="abs" role="img" aria-label="Portrait photo of expert Mira Daven" style="left:91px;top:185px;width:148px;height:148px;border-radius:50%;background:linear-gradient(160deg,#b59a86,#6e5a50)"></div>
    <p class="expert-name">MIRA DAVEN</p>
    <p class="expert-bio">Nam libero tempore, cum soluta nobi eligrendi quia<br>numquam quod maxiue place facere</p>
    <div class="social"><span></span><span></span><span></span></div>
  </div>

  <div class="expert" style="left:435px">
    <svg class="abs" style="left:73px;top:165px" width="184" height="184" aria-hidden="true"><path d="M92 8A84 84 0 0 0 30 154" fill="none" stroke="var(--blue)" stroke-width="7"/><path d="M120 12A84 84 0 0 1 92 176" fill="none" stroke="var(--purple)" stroke-width="7"/><circle cx="92" cy="94" r="78" fill="#fff"/><path d="M130 6L134 16L144 17L136 23L139 33L130 27L121 33L124 23L116 17L126 16Z" fill="#7a7a7a"/></svg>
    <div class="abs" role="img" aria-label="Portrait photo of expert Lena Corvash" style="left:91px;top:185px;width:148px;height:148px;border-radius:50%;background:linear-gradient(160deg,#c9a27a,#6a4e3a)"></div>
    <p class="expert-name active">LENA CORVASH</p>
    <p class="expert-bio">Nam libero tempore, cum soluta nobi eligrendi quia<br>numquam quod maxiue place facere</p>
    <div class="social active"><span></span><span></span><span></span></div>
  </div>

  <div class="expert" style="left:801px">
    <svg class="abs" style="left:73px;top:165px" width="184" height="184" aria-hidden="true"><path d="M92 8A84 84 0 1 1 30 34" fill="none" stroke="#fff" stroke-width="6"/><circle cx="92" cy="94" r="78" fill="#fff"/><path d="M142 0L146 10L156 11L148 17L151 27L142 21L133 27L136 17L128 11L138 10Z" fill="#fff"/></svg>
    <div class="abs" role="img" aria-label="Portrait photo of expert Tessa Rowan" style="left:91px;top:185px;width:148px;height:148px;border-radius:50%;background:linear-gradient(160deg,#b7a2b4,#4a3440)"></div>
    <p class="expert-name">TESSA ROWAN</p>
    <p class="expert-bio">Nam libero tempore, cum soluta nobi eligrendi quia<br>numquam quod maxiue place facere</p>
    <div class="social"><span></span><span></span><span></span></div>
  </div>
</section>

<footer class="site-footer">
  <nav class="footer-nav">
    <a style="left:225px">Home</a><span class="sep" style="left:304px">|</span>
    <a style="left:352px">About Us</a><span class="sep" style="left:451px">|</span>
    <a style="left:500px">Podcast</a><span class="sep" style="left:592px">|</span>
    <a style="left:638px">Contact us</a><span class="sep" style="left:748px">|</span>
    <a style="left:796px">Resource</a><span class="sep" style="left:896px">|</span>
    <a style="left:943px">Shop</a>
  </nav>
  <div class="footer-rule"></div>
  <div class="contact" style="left:259px">
    <span class="contact-icon"><svg width="16" height="16" viewBox="0 0 16 16" aria-hidden="true"><path d="M3 1L6 1L7 5L5 6.5C6 9 7 10 9.5 11L11 9L15 10V13C15 14 14 15 13 15C6.5 15 1 9.5 1 3C1 2 2 1 3 1Z" fill="var(--purple)"/></svg></span>(012) 4800 2731
  </div>
  <div class="contact" style="left:495px">
    <span class="contact-icon"><svg width="18" height="14" viewBox="0 0 18 14" aria-hidden="true"><rect x="1" y="1" width="16" height="12" rx="1.5" fill="var(--purple)"/><path d="M1.5 2L9 8L16.5 2" fill="none" stroke="#fff" stroke-width="1.5"/></svg></span>info@brightlanternharbor.com
  </div>
  <div class="contact" style="left:789px">
    <span class="contact-icon"><svg width="16" height="16" viewBox="0 0 16 16" aria-hidden="true"><rect x="2" y="5" width="12" height="10" rx="1" fill="var(--purple)"/><path d="M5 6V4A3 3 0 0 1 11 4V6" fill="none" stroke="var(--purple)" stroke-width="1.6"/></svg></span>(012) 4800 2731
  </div>
</footer>
<div class="bottom-bar">
  <p class="copyright">Copyrights © 2018, Bright Lantern Warm Harbor . All Rights Reserved.</p>
  <div class="bottom-social"><span></span><span></span><span></span><span></span><span></span></div>
</div>

</body>
</html>
```